VALMIRE/ VALMIRE NOIR Business Card

We have two brands that we would like to show one 1 business card (front and back). We would to incorporate two different logos on one card (VALMIRE and VALMIRE NOIR). Card can be two sided. Simple, sleek and professional.

We are a senior living provider.

www.valmire-example.com
www.valmirenoir-example.com

Target Market(s)

Professionals

Industry/Entity Type

Business

Font styles to use
Serif

Colors

Designer to choose colors to be used in the design.

Requirements
Must have
• Space for EMAIL, PHONE, WEBSITE
Nice to have
• Raised lettering or gloss lettering

```html
<!DOCTYPE html>
<html lang="en">
<head>
<meta charset="utf-8">
<title>VALMIRE / VALMIRE NOIR Business Card</title>
<link rel="stylesheet" href="https://fonts.googleapis.com/css2?family=Cinzel:wght@400&family=PT+Sans:wght@400&display=swap">
<style>
  :root {
    --gold: #c4912e;
    --noir: #2b2a29;
    --paper: #ffffff;
    --frame: #555555;
    --text-light: #ffffff;
  }
  html, body {
    margin: 0;
    padding: 0;
    overflow: hidden;
  }
  body {
    width: 1200px;
    height: 1200px;
    background: var(--paper);
    position: relative;
    font-family: "PT Sans", sans-serif;
  }
  .canvas-frame {
    position: absolute;
    inset: 0;
    border: 1px solid var(--frame);
    box-sizing: border-box;
  }
  .card {
    position: absolute;
    left: 260px;
    width: 679px;
    height: 423px;
    border-radius: 8px;
    box-sizing: border-box;
  }
  .card--front {
    top: 137px;
    background: var(--paper);
    border: 1px solid #333;
  }
  .card--back {
    top: 643px;
    background: var(--noir);
  }
  .brand-name {
    position: absolute;
    margin: 0;
    font-family: "Cinzel", serif;
    font-weight: 400;
    line-height: 1;
    white-space: nowrap;
    color: var(--gold);
  }
  .card--front .brand-name {
    left: 42px;
    top: 128px;
    font-size: 96px;
    letter-spacing: 2px;
  }
  .card--back .brand-name {
    left: 40px;
    top: 136px;
    font-size: 56px;
    letter-spacing: 2px;
  }
  .tagline {
    position: absolute;
    left: 42px;
    top: 200px;
    margin: 0;
    font-size: 28px;
    line-height: 1.1;
    color: var(--text-light);
    white-space: nowrap;
  }
  .divider {
    position: absolute;
    left: 40px;
    right: 40px;
    top: 362px;
    height: 1px;
    background: var(--gold);
  }
  .contact-row {
    position: absolute;
    left: 40px;
    right: 40px;
    top: 371px;
    display: flex;
    justify-content: space-between;
    gap: 14px;
    font-size: 16px;
    line-height: 1.2;
    white-space: nowrap;
  }
  .card--front .contact-row { color: var(--gold); font-size: 17px; }
  .card--back .contact-row { color: var(--text-light); font-size: 15.5px; }
</style>
</head>
<body>
  <div class="canvas-frame"></div>

  <section class="card card--front">
    <h1 class="brand-name">VALMIRE</h1>
    <div class="divider"></div>
    <div class="contact-row">
      <span class="contact-web">www.valmire-example.com</span>
      <span class="contact-email">info@valmire-example.com</span>
      <span class="contact-phone">012 640 7315</span>
    </div>
  </section>

  <section class="card card--back">
    <h2 class="brand-name">VALMIRE NOIR</h2>
    <p class="tagline">Executive Personal Care Services</p>
    <div class="divider"></div>
    <div class="contact-row">
      <span class="contact-web">www.valmirenoir-example.com</span>
      <span class="contact-email">info@valmirenoir-example.com</span>
      <span class="contact-phone">012 640 7326</span>
    </div>
  </section>
</body>
</html>
```